依頼詳細
ポスティング用のチラシです。
思わず手に取って見たくなるようなデザインとキャッチャーなコピーを
ご提案ください。

原稿にイラストを入れましたが、写真でも構いません。
また、全体のレイアウトも自由に変更頂いて構いません。

尚、コンペで表面が決まりましたら、裏面に着手していただきますので、
ご承知おきください。

それではご提案お待ちしております。
何卒よろしくお願い申し上げます。

記載項目
原稿にまとめました
サイズ
A4
ページ数
両面
希望イメージ
シンプル 複雑
単色 カラフル
暗い 明るい
日常 高級
遊び心 厳粛
未来的 伝統的
女性的 男性的
希望する色
納品ファイル
• イラストレーター形式 (.ai)
補足説明
お世話様でございます。
どれも素晴らしいご提案、誠にありがとうございました。
検討させていただきますので、決定までにしばらくお時間くださいませ。
宜しくお願い申し上げます。
■ 選んだ理由

インパクトのあるアイキャッチ(イラスト・コピー)と、非常に分かり易くまとめて頂いた所が
ポイントです。

■ 提案者全員のお礼・コメント

この度は素晴らしい作品をご提案頂きまして、誠にありがとうございました。
また機会を作りますので、今後ともよろしくお願い申し上げます。

```html
<!DOCTYPE html>
<html lang="ja">
<head>
<meta charset="utf-8">
<title>出張メガネサービス チラシ</title>
<link href="https://fonts.googleapis.com/css2?family=M+PLUS+Rounded+1c:wght@500;700;800;900&family=Noto+Sans+JP:wght@400;500;700;900&display=swap" rel="stylesheet">
<style>
:root{
  --sky:#dff1fb;
  --blue:#1a7fd0;
  --blue-dark:#0f5fa8;
  --red:#e60f1e;
  --green:#1b9a3a;
  --green-dark:#0d6e2a;
  --ink:#222;
  --grey:#666;
  --cream:#fff8e3;
  --orange:#f39800;
  --yellow:#ffef3a;
  --white:#fff;
}
*{margin:0;padding:0;box-sizing:border-box}
html,body{width:849px;height:1200px;overflow:hidden;background:var(--white)}
body{font-family:"Noto Sans JP",sans-serif;color:var(--ink)}
.flyer{position:relative;width:849px;height:1200px;overflow:hidden;background:var(--white)}

.hero{position:absolute;left:0;top:0;width:849px;height:340px;background:linear-gradient(180deg,var(--sky) 0%,var(--white) 100%)}
.person{position:absolute;top:10px;width:150px;height:160px;border-radius:50% 50% 20px 20px;background:linear-gradient(180deg,#e9d6c2,#c9b29a)}
.person--man{left:22px}
.person--woman{right:22px}
.worry{position:absolute;left:190px;top:22px;width:470px;text-align:center;font-family:"M PLUS Rounded 1c",sans-serif;font-weight:800;font-size:26px;line-height:1.35;color:var(--ink)}
.but{position:absolute;left:0;top:160px;width:849px;text-align:center;font-family:"M PLUS Rounded 1c",sans-serif;font-weight:900;font-size:60px;color:var(--red);line-height:1;text-shadow:0 3px 0 rgba(0,0,0,.12)}
.headline{position:absolute;left:0;top:226px;width:849px;text-align:center;font-family:"M PLUS Rounded 1c",sans-serif;font-weight:900;font-size:44px;line-height:1.2;color:var(--green)}
.headline span{display:block}

.steps{position:absolute;left:22px;top:346px;width:805px;display:flex;justify-content:space-between;list-style:none}
.step{width:150px;height:140px;border-radius:14px;background:var(--blue);color:var(--white);text-align:center;padding-top:8px;position:relative}
.step--free{background:var(--red);padding-top:20px}
.step__num{display:block;font-family:"M PLUS Rounded 1c",sans-serif;font-weight:900;font-size:32px;line-height:1.1}
.step__text{display:block;font-weight:700;font-size:15px;line-height:1.35;padding:4px 6px 0}
.step--free .step__text{padding-top:0;font-size:16px}
.step__free{display:block;font-weight:900;font-size:22px;color:var(--yellow);margin-top:2px}
.step:not(:last-child)::after{content:"";position:absolute;right:-11px;top:58px;border-left:9px solid var(--blue-dark);border-top:9px solid transparent;border-bottom:9px solid transparent}

.photos{position:absolute;left:22px;top:497px;width:805px;height:308px}
.photo{position:absolute;border-radius:6px}
.photo--van{left:0;top:0;width:520px;height:308px;background:linear-gradient(180deg,#cfe6f5 0%,#f4f7f9 45%,#9aa3a8 100%)}
.photo--seat{left:530px;top:0;width:275px;height:149px;background:linear-gradient(160deg,#b9c4cc,#e7eaec)}
.photo--desk{left:530px;top:159px;width:275px;height:149px;background:linear-gradient(160deg,#d8d2c5,#8e8a82)}

.note{position:absolute;left:22px;top:814px;width:805px;font-size:12px;color:var(--grey);white-space:nowrap}

.voices{position:absolute;left:22px;top:838px;width:805px;height:200px;background:var(--cream);border-radius:10px;padding:10px 18px}
.voices__title{text-align:center;font-family:"M PLUS Rounded 1c",sans-serif;font-weight:900;font-size:28px;color:var(--orange);line-height:1.2}
.voices__title::before{content:"";display:inline-block;width:20px;height:20px;border-radius:50%;background:var(--orange);margin-right:8px;vertical-align:-2px}
.voices__list{display:flex;gap:24px;margin-top:10px}
.voice{flex:1}
.voice__who{font-weight:700;font-size:15px;color:var(--ink);border-bottom:2px dotted var(--orange);padding-bottom:3px;margin-bottom:6px}
.voice__body{font-size:13px;line-height:1.6;color:var(--ink)}

.footer{position:absolute;left:0;top:1050px;width:849px;height:150px;background:var(--white);border-top:4px solid var(--blue)}
.brand{position:absolute;left:22px;top:34px;display:flex;align-items:center;gap:10px}
.brand__dot{width:48px;height:48px;border-radius:50%;background:var(--orange)}
.brand__name{font-weight:900;font-size:18px;line-height:1.3;color:var(--ink)}
.contact{position:absolute;left:232px;top:10px;width:380px;text-align:center}
.contact__lead{font-family:"M PLUS Rounded 1c",sans-serif;font-weight:900;font-size:26px;line-height:1.25;color:var(--blue-dark)}
.contact__addr{text-align:right;font-size:13px;color:var(--ink);margin-top:2px;padding-right:16px}
.contact__tel{display:flex;align-items:center;justify-content:center;gap:6px;font-weight:900;font-size:34px;color:var(--green-dark);line-height:1.1}
.safety{position:absolute;right:22px;top:16px;width:200px;height:118px;background:var(--green);border-radius:6px;color:var(--white);text-align:center;padding-top:8px}
.safety__title{font-weight:900;font-size:16px}
.safety__icons{display:flex;justify-content:center;flex-wrap:wrap;gap:10px;margin-top:10px;padding:0 30px}
.safety__icons span{width:32px;height:32px;border-radius:50%;background:var(--white);opacity:.9}
</style>
</head>
<body>
<main class="flyer">
  <section class="hero">
    <div class="person person--man" role="img" aria-label="困った表情の年配の男性のイラスト"></div>
    <div class="person person--woman" role="img" aria-label="困った表情の年配の女性のイラスト"></div>
    <p class="worry">メガネがほしいけど<br>新型コロナウイルスが<br>心配でお店に行けない…</p>
    <p class="but">でも!</p>
    <h1 class="headline"><span>お店にいかなくても大丈夫!</span><span>専用車でご自宅まで伺います!</span></h1>
  </section>

  <ol class="steps">
    <li class="step"><span class="step__num">1</span><span class="step__text">視力測定<br>車両で<br>ご自宅に到着</span></li>
    <li class="step"><span class="step__num">2</span><span class="step__text">車内で<br>視力検査</span></li>
    <li class="step"><span class="step__num">3</span><span class="step__text">レンズ・<br>フレームを<br>お選びいただきます</span></li>
    <li class="step"><span class="step__num">4</span><span class="step__text">注文後、会社や<br>ご自宅に<br>お届けします</span></li>
    <li class="step step--free"><span class="step__text">視力測定<br>超音波洗浄<br>ネジ・調整</span><span class="step__free">無料</span></li>
  </ol>

  <div class="photos">
    <div class="photo photo--van" role="img" aria-label="視力測定専用車両(白いワゴン車)の写真"></div>
    <div class="photo photo--seat" role="img" aria-label="車内の視力測定席の写真"></div>
    <div class="photo photo--desk" role="img" aria-label="車内のレンズ・フレーム選びスペースの写真"></div>
  </div>

  <p class="note">※レンズメーカーは、主要国内メーカーの商品を取り扱っております。男性用・女性用など各種取り揃えております。</p>

  <section class="voices">
    <h2 class="voices__title">お客様の声</h2>
    <div class="voices__list">
      <article class="voice">
        <p class="voice__who">長野市中御所 C様(70代男性)</p>
        <p class="voice__body">外出が心配でしたが、自宅の前まで来てもらえて安心しました。車内でゆっくり検査してもらい、新しいメガネもよく見えて大満足です。</p>
      </article>
      <article class="voice">
        <p class="voice__who">長野市 A様(60代女性)</p>
        <p class="voice__body">仕事の合間に会社まで来ていただき助かりました。フレームの種類も多く、丁寧に相談にのってくれたので、また利用したいです。</p>
      </article>
    </div>
  </section>

  <footer class="footer">
    <div class="brand">
      <span class="brand__dot"></span>
      <p class="brand__name">株式会社 ミルメ<br>めがねのミルメ</p>
    </div>
    <div class="contact">
      <p class="contact__lead">メガネのことなら<br>何でもご相談ください!</p>
      <p class="contact__addr">長野市緑町123</p>
      <p class="contact__tel">
        <svg width="28" height="28" viewBox="0 0 24 24" aria-hidden="true"><path fill="#0d6e2a" d="M6.6 10.8a15.1 15.1 0 0 0 6.6 6.6l2.2-2.2c.3-.3.7-.4 1-.2 1.1.4 2.3.6 3.6.6.6 0 1 .4 1 1V20c0 .6-.4 1-1 1A17 17 0 0 1 3 4c0-.6.4-1 1-1h3.5c.6 0 1 .4 1 1 0 1.3.2 2.5.6 3.6.1.3 0 .7-.2 1z"/></svg>
        0120-00-4567
      </p>
    </div>
    <div class="safety">
      <p class="safety__title">感染症対策強化中</p>
      <div class="safety__icons"><span></span><span></span><span></span><span></span></div>
    </div>
  </footer>
</main>
</body>
</html>
```